Enhance the web site presence of KRU Global Limited

Upgrade the current web site www.krucircuit-example.com to share with the audience our current plan and future developments of our company. I have created a worksheet which shows all the pages that I like to have. The home page in English, Japanese and Chinese is hyperlinked to the various pages. Under the product, we should allow the user to select "single sided PCB or double sided PCB". The translation of the contents of the pages with Japanese is not complete but the English and Chinese are complete. You can download the briefing and photos in the dropbox files below;

https://www.filebinvault-example.com/sh/x7k2mq9plw4rt8a/BBQZ_Hn462UdgnRtYmXzzYfLb?dl=0

Target Market(s)

Electronic companies

Industry/Entity Type

Electronic

Coding

Coded - Design and coding required

Number of Pages Required

5+ page

Font styles to use
Sans Serif

Colors
00a990
0353a1
33b8a4

Requirements
Must have
• Get a sense of confidence on our company's integrity and capability to deliver the highest quality PCBs with the most competitive prices and best services. A sense of elegance is essential as we DON'T treat profits as the number one goal. Our number goal is to do the RIGHT things right. Having a mixture of our company photos will be appropriate.

```html
<!DOCTYPE html>
<html lang="en">
<head>
<meta charset="utf-8">
<title>KRU Global Limited</title>
<link rel="stylesheet" href="https://fonts.googleapis.com/css2?family=Montserrat:wght@400;600;700&family=Open+Sans:wght@400;600&display=swap">
<style>
:root{
  --teal:#00a990;
  --teal-light:#33b8a4;
  --blue:#0353a1;
  --ink:#2b2b2b;
  --muted:#8a8a8a;
  --page:#f7f7f7;
  --bar:#262626;
  --hero-a:#9fb0b4;
  --hero-b:#d8dedf;
  --meeting-a:#b9c4cf;
  --meeting-b:#e4e8ec;
}
*{box-sizing:border-box;margin:0;padding:0}
html,body{width:679px;height:1200px;overflow:hidden;background:var(--page)}
body{font-family:'Montserrat',sans-serif;color:var(--ink);position:relative}
.topbar{position:absolute;top:0;left:0;width:679px;height:14px;background:var(--bar);color:#fff;font-family:'Open Sans',sans-serif;font-size:6.5px;display:flex;justify-content:flex-end;align-items:center;gap:10px;padding-right:77px}
.header{position:absolute;top:14px;left:0;width:679px;height:40px;background:#fff;border-bottom:1px solid #e6e6e6}
.brand{position:absolute;left:74px;top:11px;display:flex;align-items:center;gap:5px;font-family:'Montserrat',sans-serif;font-weight:700;font-size:15px;color:var(--blue);letter-spacing:1px}
.brand .mark{width:9px;height:9px;background:var(--blue)}
.nav{position:absolute;left:246px;top:15px;display:flex;gap:11px;font-family:'Open Sans',sans-serif;font-size:7px;color:#777}
.nav .active{color:var(--teal);border-bottom:1px solid var(--teal);padding-bottom:4px}
.hero{position:absolute;top:54px;left:0;width:679px;height:279px;background:linear-gradient(180deg,var(--hero-a),var(--hero-b) 55%,#7f8a8c)}
.hero-band{position:absolute;left:0;bottom:0;width:100%;height:60px;background:rgba(40,40,40,.55)}
.hero-title{position:absolute;top:120px;width:100%;text-align:center;font-family:'Open Sans',sans-serif;font-weight:600;font-size:25px;color:#fff;text-shadow:0 1px 3px rgba(0,0,0,.35)}
.hero-arrow{position:absolute;top:146px}
.about{position:absolute;top:333px;left:0;width:679px;height:633px;background:var(--page)}
.section-title{text-align:center;font-weight:700;font-size:27px;background:linear-gradient(90deg,var(--teal-light),var(--blue));-webkit-background-clip:text;background-clip:text;color:transparent}
.rule{width:40px;height:2px;background:var(--blue);margin:0 auto}
.about .section-title{position:absolute;top:64px;width:100%}
.about .rule{position:absolute;top:115px;left:319px}
.about-text{position:absolute;top:132px;left:210px;width:260px;text-align:center;font-size:6.5px;line-height:13px;color:var(--muted)}
.card{position:absolute;top:231px;width:169px;height:204px;border:1px solid var(--blue)}
.card::before{content:"";position:absolute;left:-3px;top:-3px;right:3px;bottom:3px;border:1px solid var(--teal-light)}
.card svg{position:absolute;left:72px;top:28px}
.card p{position:absolute;top:68px;left:21px;width:128px;font-size:6.2px;line-height:13.3px;color:var(--muted)}
.btn{position:absolute;display:flex;align-items:center;justify-content:center;gap:6px;height:21px;font-size:6px;font-weight:700;letter-spacing:.4px;color:#fff;background:linear-gradient(90deg,var(--teal-light),var(--blue))}
.card .btn{top:156px;left:46px;width:76px}
.clients .section-title{position:absolute;top:820px;width:100%}
.clients .rule{position:absolute;top:868px;left:319px}
.logos{position:absolute;top:885px;left:102px;width:475px;display:flex;justify-content:space-between;align-items:center}
.logo-name{width:103px;height:54px;display:flex;align-items:center;justify-content:center;gap:5px;font-family:'Montserrat',sans-serif;font-weight:700;font-size:14px;color:var(--blue)}
.logo-name .dot{width:10px;height:10px;border-radius:50%;background:var(--blue)}
.contact{position:absolute;top:966px;left:0;width:679px;height:215px;background:linear-gradient(135deg,var(--meeting-a),var(--meeting-b) 60%,#aeb8c2)}
.contact-slant{position:absolute;top:0;left:0}
.contact h2{position:absolute;top:72px;width:100%;text-align:center;font-weight:700;font-size:26px;color:#fff;text-shadow:0 1px 3px rgba(0,0,0,.3)}
.contact .btn{top:124px;left:301px;width:77px;background:rgba(30,40,50,.35);border:1px solid var(--teal-light)}
.footer{position:absolute;top:1181px;left:0;width:679px;height:19px;background:var(--bar);color:#999;font-size:5.8px;display:flex;align-items:center;justify-content:center}
</style>
</head>
<body>
<div class="topbar"><span>Mail: sales@krucircuit-example.com</span><span>Tel: (852) 5550 2184</span></div>

<header class="header">
  <div class="brand"><span class="mark"></span>KRU</div>
  <nav class="nav"><span class="active">Home</span><span>Products</span><span>Our Facility</span><span>Customers</span><span>Contact</span></nav>
</header>

<section class="hero" role="img" aria-label="Photo of the KRU factory building with rooftop signage">
  <div class="hero-band"></div>
  <h1 class="hero-title">Welcome to KRU Global Limited</h1>
  <svg class="hero-arrow" style="left:7px" width="8" height="12" viewBox="0 0 8 12"><path d="M6 1 1 6l5 5" fill="none" stroke="#fff" stroke-width="1.2"/></svg>
  <svg class="hero-arrow" style="left:664px" width="8" height="12" viewBox="0 0 8 12"><path d="M2 1l5 5-5 5" fill="none" stroke="#fff" stroke-width="1.2"/></svg>
</section>

<section class="about">
  <h2 class="section-title">About us</h2>
  <div class="rule"></div>
  <p class="about-text">KRU Global Limited is a Hong Kong based company specializing in single and double sided printed circuit boards. Its manufacturing facility is located in a self-owned facility in Guangdong, China which is close to Hong Kong.</p>

  <div class="card" style="left:73px">
    <svg width="24" height="24" viewBox="0 0 24 24"><path d="M12 2l3 7h7l-5.5 4.5 2 7.5L12 16.5 5.5 21l2-7.5L2 9h7z" fill="none" stroke="var(--blue)" stroke-width="1"/></svg>
    <p>Our mission is to become a premium low costs PCB supplier that fully embraces human, social and environmental responsibilities.</p>
    <span class="btn">READ MORE <svg width="9" height="7" viewBox="0 0 9 7"><path d="M0 3.5h8M5 .5l3 3-3 3" fill="none" stroke="#fff"/></svg></span>
  </div>
  <div class="card" style="left:255px">
    <svg width="24" height="24" viewBox="0 0 24 24"><path d="M14 2 7 13h5l-2 9 7-12h-5z" fill="none" stroke="var(--blue)" stroke-width="1"/></svg>
    <p>Through our insatiable drive to maximize efficiency, KRU is becoming a highly efficient PCB factory with a capacity of 140,000 square meter a month.</p>
    <span class="btn">READ MORE <svg width="9" height="7" viewBox="0 0 9 7"><path d="M0 3.5h8M5 .5l3 3-3 3" fill="none" stroke="#fff"/></svg></span>
  </div>
  <div class="card" style="left:436px">
    <svg width="24" height="24" viewBox="0 0 24 24"><path d="M4 21v-6h3v6zM10 21v-9h3v9zM16 21V7h3v14zM4 10l6-5 3 2 6-5" fill="none" stroke="var(--blue)" stroke-width="1"/></svg>
    <p>PCB is our business and it is through continued automation and innovation that will drive our growth in the next 10 years.</p>
    <span class="btn">READ MORE <svg width="9" height="7" viewBox="0 0 9 7"><path d="M0 3.5h8M5 .5l3 3-3 3" fill="none" stroke="#fff"/></svg></span>
  </div>
</section>

<section class="clients">
  <h2 class="section-title">Our Clients</h2>
  <div class="rule"></div>
  <div class="logos">
    <div class="logo-name"><span class="dot"></span>Norvalt</div>
    <div class="logo-name">Kessho</div>
    <div class="logo-name">Lumarek</div>
    <div class="logo-name"><span class="dot"></span>Aventi</div>
  </div>
</section>

<section class="contact" role="img" aria-label="Photo of a business team meeting around a table with a laptop and documents">
  <svg class="contact-slant" width="679" height="22" viewBox="0 0 679 22"><path d="M0 0h679v8L0 22z" fill="var(--page)"/></svg>
  <h2>Get in touch</h2>
  <span class="btn">CONTACT US <svg width="9" height="7" viewBox="0 0 9 7"><path d="M0 3.5h8M5 .5l3 3-3 3" fill="none" stroke="#fff"/></svg></span>
</section>

<footer class="footer">© 2018. KRU Global Limited</footer>
</body>
</html>
```